Vantrel Ashcombe LLC

we need a business card design

Industry/Entity Type

hvac

Contact Information for Business Card

my logo

Requirements
Must have
• my logo and same colors

```html
<!DOCTYPE html>
<html lang="en">
<head>
<meta charset="utf-8">
<title>Vantrel Ashcombe LLC — Business Card</title>
<link rel="stylesheet" href="https://fonts.googleapis.com/css2?family=Open+Sans:wght@400;700&display=swap">
<style>
  :root {
    --canvas-bg: #e9e6e1;
    --navy-deep: #04244d;
    --navy-mid: #0a4a8a;
    --brand-blue: #15579f;
    --brand-gold: #f2a62b;
    --text-grey: #4a4a4a;
    --card-white: #ffffff;
    --card-edge: #f1f1f1;
    --divider: #2a3f7a;
  }
  * { margin: 0; padding: 0; box-sizing: border-box; }
  html, body {
    width: 1200px;
    height: 900px;
    overflow: hidden;
    background: var(--canvas-bg);
    font-family: "Open Sans", sans-serif;
  }
  .canvas {
    width: 1200px;
    height: 900px;
    display: flex;
    flex-direction: column;
    align-items: center;
    justify-content: center;
    gap: 40px;
  }
  .card {
    width: 630px;
    height: 360px;
    border-radius: 28px;
    box-shadow: 0 10px 28px rgba(0,0,0,0.18);
    position: relative;
    overflow: hidden;
  }
  /* Front side */
  .card-front {
    background: radial-gradient(ellipse at 50% 45%, var(--navy-mid) 0%, #073b74 40%, var(--navy-deep) 100%);
    display: flex;
    align-items: center;
    justify-content: center;
  }
  .brand-lockup {
    display: flex;
    align-items: center;
    gap: 14px;
  }
  .brand-dot {
    width: 22px;
    height: 22px;
    border-radius: 50%;
    background: var(--brand-gold);
    flex: none;
  }
  .brand-name {
    font-weight: 700;
    font-size: 30px;
    line-height: 1.15;
    color: var(--card-white);
    text-align: left;
  }
  /* Back side */
  .card-back {
    background: linear-gradient(120deg, var(--card-edge) 0%, var(--card-white) 60%, var(--card-white) 100%);
    display: grid;
    grid-template-columns: 320px 1px 1fr;
    align-items: center;
  }
  .card-back .brand-lockup { justify-self: center; }
  .card-back .brand-name { color: var(--brand-blue); font-size: 26px; }
  .divider {
    width: 1px;
    height: 250px;
    background: linear-gradient(180deg, rgba(42,63,122,0) 0%, var(--divider) 50%, rgba(42,63,122,0) 100%);
  }
  .contact-block { padding-left: 34px; }
  .person-name {
    font-weight: 700;
    font-size: 21px;
    color: var(--brand-blue);
    letter-spacing: 0.3px;
  }
  .person-title {
    font-size: 14px;
    color: var(--text-grey);
    margin-bottom: 18px;
  }
  .contact-list { list-style: none; }
  .contact-item {
    display: flex;
    align-items: center;
    gap: 10px;
    font-size: 14px;
    color: var(--text-grey);
    margin-bottom: 8px;
  }
  .contact-item svg { width: 16px; height: 16px; flex: none; }
  .domain { color: var(--brand-gold); }
  .address {
    margin-top: 16px;
    padding-left: 26px;
    font-size: 14px;
    line-height: 1.35;
    color: var(--text-grey);
  }
</style>
</head>
<body>
<main class="canvas">
  <section class="card card-front" aria-label="Card front">
    <div class="brand-lockup">
      <span class="brand-dot"></span>
      <span class="brand-name">Vantrel Ashcombe LLC</span>
    </div>
  </section>

  <section class="card card-back" aria-label="Card back">
    <div class="brand-lockup">
      <span class="brand-dot"></span>
      <span class="brand-name">Vantrel<br>Ashcombe LLC</span>
    </div>
    <div class="divider"></div>
    <div class="contact-block">
      <h1 class="person-name">DORIAN PELLWAY</h1>
      <p class="person-title">Director</p>
      <ul class="contact-list">
        <li class="contact-item">
          <svg viewBox="0 0 16 16" aria-hidden="true"><path fill="#f2a62b" d="M3.6 1.5l2.2 2.6-1.3 1.6c.9 2 2.4 3.6 4.4 4.6l1.6-1.3 2.6 2.2-1.3 2.3c-5.6-.6-9.6-4.8-10.2-10.2z"/></svg>
          <span>300-555-0147</span>
        </li>
        <li class="contact-item">
          <svg viewBox="0 0 16 16" aria-hidden="true"><rect x="1" y="3.5" width="14" height="9" rx="1" fill="#f2a62b"/><path d="M1.5 4l6.5 5 6.5-5" fill="none" stroke="#fff" stroke-width="1.2"/></svg>
          <span>info@<span class="domain">vantrelashcombe</span>.com</span>
        </li>
        <li class="contact-item">
          <svg viewBox="0 0 16 16" aria-hidden="true"><g fill="none" stroke="#f2a62b" stroke-width="1.2"><circle cx="8" cy="8" r="6.5"/><ellipse cx="8" cy="8" rx="2.8" ry="6.5"/><path d="M1.5 8h13M2.5 4.8h11M2.5 11.2h11"/></g></svg>
          <span>www.<span class="domain">vantrelashcombe</span>.com</span>
        </li>
      </ul>
      <p class="address">00 dummy city<br>dummy place 0000</p>
    </div>
  </section>
</main>
</body>
</html>
```